Pebble

My company name is pebble. The logo is attached. I am the business owner.
Name Gideon Thorpe
Phone number- 5553018826
email- Gideon_thorpe@quillnet.net
Website is not live yet but it will be workwithpebble.com
the current beta link is- https://site.brvhosting.com/pebble-v3/
on the back write “ find creative pros”
Use that beta link as reference for typography and colors on card.

```html
<!DOCTYPE html>
<html lang="en">
<head>
<meta charset="utf-8">
<title>Pebble — Business Card</title>
<link rel="stylesheet" href="https://fonts.googleapis.com/css2?family=Montserrat:wght@700;800&family=Arimo:wght@400&display=swap">
<style>
  :root {
    --bg: #161616;
    --card: #2f2f2f;
    --card-front: #2c2c2c;
    --orange: #d4531c;
    --logo-light: #e6e6e6;
    --logo-dark: #1e1e1e;
    --text-light: #d8d8d8;
    --divider: #4a4a4a;
  }
  * { margin: 0; padding: 0; box-sizing: border-box; }
  html, body {
    width: 1200px; height: 900px; overflow: hidden;
    background: var(--bg);
  }
  .canvas {
    position: relative; width: 1200px; height: 900px;
    background: radial-gradient(ellipse at 50% 45%, #2a2a2a 0%, var(--bg) 75%);
  }
  .card {
    position: absolute; left: 320px; width: 560px; height: 320px;
    border-radius: 2px;
    box-shadow: 0 18px 40px rgba(0,0,0,0.55);
  }
  .card--front { top: 90px; background: var(--card-front); }
  .card--back { top: 480px; background: var(--card); }

  .front-brand {
    position: absolute; inset: 0;
    display: flex; flex-direction: column; align-items: center; justify-content: center;
  }
  .wordmark {
    font-family: "Montserrat", sans-serif; font-weight: 800;
    text-transform: uppercase; letter-spacing: 1px; line-height: 1;
  }
  .front-brand .wordmark { font-size: 64px; color: var(--logo-dark); }
  .tagline {
    margin-top: 12px;
    font-family: "Montserrat", sans-serif; font-weight: 700;
    font-size: 19px; color: var(--orange); letter-spacing: 0.5px;
  }

  .back-brand {
    position: absolute; left: 40px; top: 0; bottom: 0; width: 240px;
    display: flex; align-items: center; justify-content: center;
  }
  .back-brand .wordmark { font-size: 50px; color: var(--logo-light); }
  .divider {
    position: absolute; left: 300px; top: 70px; width: 1px; height: 180px;
    background: linear-gradient(to bottom, transparent, var(--divider), transparent);
  }
  .contact {
    position: absolute; left: 325px; top: 92px;
    font-family: "Arimo", sans-serif; color: var(--text-light);
  }
  .contact-name {
    font-family: "Montserrat", sans-serif; font-weight: 700;
    font-size: 19px; color: var(--orange); letter-spacing: 0.5px;
    margin-bottom: 14px;
  }
  .contact-list { list-style: none; }
  .contact-item {
    display: flex; align-items: center; gap: 8px;
    font-size: 13.5px; margin-bottom: 8px;
  }
  .contact-icon {
    width: 22px; height: 22px; border-radius: 50%;
    background: var(--orange); flex: none;
    display: flex; align-items: center; justify-content: center;
  }
  .contact-icon svg { width: 12px; height: 12px; }
</style>
</head>
<body>
<main class="canvas">
  <section class="card card--front" aria-label="Card front">
    <div class="front-brand">
      <span class="wordmark">Pebble</span>
      <p class="tagline">FIND CREATIVE PROS</p>
    </div>
  </section>

  <section class="card card--back" aria-label="Card back">
    <div class="back-brand"><span class="wordmark">Pebble</span></div>
    <div class="divider"></div>
    <div class="contact">
      <h1 class="contact-name">GIDEON THORPE</h1>
      <ul class="contact-list">
        <li class="contact-item">
          <span class="contact-icon">
            <svg viewBox="0 0 24 24" fill="none" stroke="#2f2f2f" stroke-width="2.4" stroke-linecap="round" stroke-linejoin="round"><path d="M22 16.9v3a2 2 0 0 1-2.2 2 19.8 19.8 0 0 1-8.6-3.1 19.5 19.5 0 0 1-6-6A19.8 19.8 0 0 1 2.1 4.2 2 2 0 0 1 4.1 2h3a2 2 0 0 1 2 1.7c.1.9.4 1.8.7 2.7a2 2 0 0 1-.5 2.1L8 9.8a16 16 0 0 0 6 6l1.3-1.3a2 2 0 0 1 2.1-.4c.9.3 1.8.6 2.7.7a2 2 0 0 1 1.7 2z"/></svg>
          </span>
          5553018826
        </li>
        <li class="contact-item">
          <span class="contact-icon">
            <svg viewBox="0 0 24 24" fill="none" stroke="#2f2f2f" stroke-width="2.4" stroke-linejoin="round"><rect x="2" y="5" width="20" height="14" rx="1"/><path d="M2 6l10 7 10-7"/></svg>
          </span>
          Gideon_thorpe@quillnet.net
        </li>
        <li class="contact-item">
          <span class="contact-icon">
            <svg viewBox="0 0 24 24" fill="none" stroke="#2f2f2f" stroke-width="2.2"><circle cx="12" cy="12" r="10"/><path d="M2 12h20M12 2a15 15 0 0 1 0 20M12 2a15 15 0 0 0 0 20"/></svg>
          </span>
          www.workwithpebble.com
        </li>
      </ul>
    </div>
  </section>
</main>
</body>
</html>
```